Business Card Project for Firm Deck Hoisting

Business name is "Firm Deck Hoisting" we are a scaffolding & rigging business specialising in local and remote work for:
- scaffolding (residential, commercial, industrial)
- rigging
-man material hoists
- swing stages
- labour hire

On the back of the card I would like FDH as the symbol / logo. I have attached the logos we have had created by sketch harbour. We would like to use bold colours – preferably as the same colour scheme as the logo.

Target Market(s)

Construction business

Industry/Entity Type

Construction

Contact Information for Business Card

name: Owen Pellew
Title: Director
Phone: 0491 572 864
Address: PO BOX 3251, Kellmore SA 5190
Email: owen@firmdeckhoisting.com.au
Website: www.firmdeckhoisting.com.au

Font styles to use
Sans Serif

Requirements
Must have
• Must use existing logo & prefering using bold colours
Nice to have
• Would be nice to have a line of dot points in what we specialise in but not essential
• Would be nice to see some designs with a slogan but not essential
Should not have
• NA

```html
<!DOCTYPE html>
<html lang="en">
<head>
<meta charset="utf-8">
<title>Firm Deck Hoisting – Business Card</title>
<link rel="stylesheet" href="https://fonts.googleapis.com/css2?family=Montserrat:wght@400;700&family=Questrial&display=swap">
<style>
  :root {
    --stage: #4a4a4a;
    --brand-blue: #2f5fbf;
    --ink: #111111;
    --card-black: #0d0d0f;
    --card-white: #f4f4f4;
    --arc-grey: #9a9a9a;
    --text-light: #ffffff;
  }
  html, body {
    margin: 0;
    padding: 0;
    width: 1200px;
    height: 869px;
    overflow: hidden;
    background: var(--stage);
  }
  .canvas {
    position: relative;
    width: 1200px;
    height: 869px;
  }
  .card {
    position: absolute;
    top: 280px;
    width: 540px;
    height: 310px;
    border-radius: 4px;
    overflow: hidden;
    box-shadow: 0 8px 22px rgba(0,0,0,0.35);
  }
  .card--front { left: 40px; }
  .card--back { left: 620px; }
  .card__art {
    position: absolute;
    inset: 0;
    width: 100%;
    height: 100%;
  }
  .wordmark {
    position: absolute;
    display: flex;
    align-items: center;
    gap: 10px;
    font-family: "Montserrat", sans-serif;
    font-weight: 700;
    letter-spacing: 1.5px;
    text-transform: uppercase;
    white-space: nowrap;
  }
  .wordmark__square {
    width: 22px;
    height: 22px;
    background: var(--brand-blue);
  }
  .card--front .wordmark {
    left: 150px;
    top: 44px;
    font-size: 22px;
    color: var(--ink);
  }
  .card--back .wordmark {
    left: 120px;
    top: 118px;
    font-size: 26px;
    color: var(--text-light);
  }
  .card--back .wordmark__square { width: 26px; height: 26px; }
  .person {
    position: absolute;
    right: 34px;
    top: 150px;
    text-align: right;
    font-family: "Montserrat", sans-serif;
  }
  .person__name {
    font-size: 24px;
    color: var(--ink);
    letter-spacing: 0.5px;
    white-space: nowrap;
  }
  .person__name b { font-weight: 700; }
  .person__role {
    font-family: "Questrial", sans-serif;
    font-size: 19px;
    color: var(--brand-blue);
    margin-top: 2px;
  }
  .contact {
    position: absolute;
    left: 16px;
    top: 204px;
    margin: 0;
    padding: 0;
    list-style: none;
    font-family: "Questrial", sans-serif;
    font-size: 11px;
    line-height: 18px;
    color: var(--text-light);
  }
  .contact li {
    display: flex;
    align-items: center;
    gap: 6px;
    white-space: nowrap;
  }
  .contact svg { width: 11px; height: 11px; flex: none; }
</style>
</head>
<body>
<main class="canvas">

  <section class="card card--front" aria-label="Business card front">
    <svg class="card__art" viewBox="0 0 540 310" aria-hidden="true">
      <rect width="540" height="310" fill="var(--brand-blue)"/>
      <ellipse cx="440" cy="20" rx="312" ry="310" fill="var(--arc-grey)"/>
      <ellipse cx="444" cy="16" rx="300" ry="298" fill="var(--card-white)"/>
      <path d="M440 0 L540 0 L540 110 Q510 30 440 0 Z" fill="var(--arc-grey)"/>
      <path d="M458 0 L540 0 L540 92 Q515 28 458 0 Z" fill="var(--brand-blue)"/>
    </svg>

    <div class="wordmark">
      <span class="wordmark__square"></span>
      <span>Firm Deck Hoisting</span>
    </div>

    <div class="person">
      <div class="person__name"><b>OWEN</b> PELLEW</div>
      <div class="person__role">Director</div>
    </div>

    <ul class="contact">
      <li>
        <svg viewBox="0 0 12 12"><circle cx="6" cy="6" r="6" fill="#fff"/><path d="M4 3 L5 3 L5.6 4.6 L4.9 5.2 Q5.5 6.6 6.8 7.1 L7.4 6.4 L9 7 L9 8 Q8 9.2 6 8 Q3.6 6.5 3.6 4 Z" fill="var(--brand-blue)"/></svg>
        <span>0491 572 864</span>
      </li>
      <li>
        <svg viewBox="0 0 12 12"><circle cx="6" cy="6" r="6" fill="#fff"/><rect x="3" y="4" width="6" height="4.2" fill="none" stroke="var(--brand-blue)" stroke-width="0.9"/><path d="M3 4 L6 6.4 L9 4" fill="none" stroke="var(--brand-blue)" stroke-width="0.9"/></svg>
        <span>owen@firmdeckhoisting.com.au</span>
      </li>
      <li>
        <svg viewBox="0 0 12 12"><circle cx="6" cy="6" r="6" fill="#fff"/><circle cx="6" cy="6" r="3.2" fill="none" stroke="var(--brand-blue)" stroke-width="0.9"/><path d="M2.8 6 H9.2 M6 2.8 V9.2" stroke="var(--brand-blue)" stroke-width="0.8"/></svg>
        <span>www.firmdeckhoisting.com.au</span>
      </li>
      <li>
        <svg viewBox="0 0 12 12"><circle cx="6" cy="6" r="6" fill="#fff"/><path d="M6 2.6 Q8.4 2.6 8.4 5 Q8.4 6.6 6 9.4 Q3.6 6.6 3.6 5 Q3.6 2.6 6 2.6 Z" fill="var(--brand-blue)"/><circle cx="6" cy="5" r="0.9" fill="#fff"/></svg>
        <span>PO BOX 3251, Kellmore SA 5190</span>
      </li>
    </ul>
  </section>

  <section class="card card--back" aria-label="Business card back">
    <svg class="card__art" viewBox="0 0 540 310" aria-hidden="true">
      <rect width="540" height="310" fill="var(--brand-blue)"/>
      <ellipse cx="300" cy="70" rx="352" ry="240" fill="var(--arc-grey)"/>
      <ellipse cx="304" cy="64" rx="340" ry="230" fill="var(--card-black)"/>
      <path d="M430 0 L540 0 L540 110 Q505 30 430 0 Z" fill="var(--arc-grey)"/>
      <path d="M448 0 L540 0 L540 92 Q510 26 448 0 Z" fill="var(--brand-blue)"/>
    </svg>

    <div class="wordmark">
      <span class="wordmark__square"></span>
      <span>Firm Deck Hoisting</span>
    </div>
  </section>

</main>
</body>
</html>
```